Marlowe's Cocktail Bar & Cigar Lounge

PLEASE DO NOT START WORKING ON THIS PROJECT BEFORE YOU READ ALL OF THE TEXT!!!
Project Title
Marlowe’s Cocktail Bar & Cigar Lounge — Full Website Design (Wix)
Project Overview
We are seeking a designer to create a sophisticated, 1920s-inspired website for Marlowe’s Cocktail Bar & Cigar Lounge, located in Kilchberg, Zurichsee, Switzerland. The site will be built on Wix and must include an art deco, luxury look, clear booking functionality, and downloadable menu.

Brand & Visual Direction
Brand: Marlowe’s Cocktail Bar & Cigar Lounge
Style: 1920s-inspired, art deco, sophisticated luxury, timeless, exclusive, subtle spectacle
Color Palette: Emerald green, gold, black, cream
Icons/Motifs: Martini glass, cigar, champagne flute, art deco borders, geometric patterns
Typography: Elegant serif for headlines (e.g., Playfair Display, Cormorant Garamond); clean sans-serif for body (e.g., Lato, Open Sans, Montserrat)
Image Style: Moody, warm lighting; classic cocktails; vintage barware; subtle 1920s hints; lounge ambiance; cigars; elegant guests
Sitemap & Main Pages
Home
About
Events
Menu
Gallery
Reservations
Contact
Website Copy
Home
Zurich’s Most Exclusive Cocktail Bar & Cigar Lounge

Timeless sophistication. Intelligent indulgence. A sanctuary by the lake.

[Reserve Your Table] (CTA Button)
A New Era on the Lake

Marlowe’s invites you into a world where elegance meets camaraderie, and every visit feels like a privilege. Step through our doors and discover a connoisseur’s sanctuary inspired by the golden age of the 1920s—reimagined for Zurich’s most discerning guests.
Signature Experiences Await
Ladies Night, Every Friday: Two cocktails for the price of one, exclusively for the ladies.
Saturday Event Series: Oyster Night, Pata Negra Night, Champagne & Caviar Night, and Vintage Havana Night—each a celebration of taste and refinement.
Curated Cocktails & Cigars: Savor our expertly crafted cocktails, rare spirits, and a handpicked selection of premium cigars.
Meet Your Hosts

In 2025, a new partnership brings fresh energy to Marlowe’s. Hospitality expert Orla Vantrisk (Quillhaven Productions) joins forces with renowned bar professional Teodor Brask (Shaker at the Ready) to elevate your experience and set a new standard for luxury in Zurichsee.
Gallery Preview

[Slideshow or mosaic of atmospheric images: cocktails, lounge ambiance, cigars, elegant guests]
Reserve Your Table

Secure your place at Zurich’s most exclusive bar.

Phone: 076 431 87 52

Email: contact@marlowes-example.ch

Online: www.marlowes-example.ch
Footer:

Uferweg 14, 8999 Seeborn, Switzerland

Open Wednesday–Sunday, 18:00–01:00 | November–April
About
Our Story

Marlowe’s Cocktail Bar & Cigar Lounge was born from a passion for refined hospitality and a love for the timeless rituals of the world’s great bars. Inspired by the golden age of the 1920s, our lounge is a haven for those who appreciate intelligent indulgence, subtle spectacle, and genuine connection.
A New Chapter: Partnership & Vision

After two successful seasons under the expert hand of Teodor Brask (Shaker at the Ready), 2025 marks a new era. Teodor has joined forces with Orla Vantrisk, Founder and creative director of Quillhaven Productions, to take Marlowe’s to even greater heights.
Together, Orla and Teodor bring decades of experience in luxury hospitality and event management. Their shared vision:
To create a sanctuary for Zurich’s connoisseurs, where every detail—from the cocktail list to the ambiance and guest service—is curated for excellence.
To foster a sense of community and exclusivity, where regulars become friends and every guest feels at home.
Our Philosophy

At Marlowe’s, we believe in:
Timeless Sophistication
Personalized Service
Intelligent Indulgence
Join Us

We invite you to experience Marlowe’s—a place where tradition is honored, innovation is celebrated, and every night is an occasion.
Events
Signature Events at Marlowe’s

At Marlowe’s Cocktail Bar & Cigar Lounge, every week is an invitation to indulge in something extraordinary.
Ladies Night – Every Friday

Every Friday, ladies enjoy two cocktails for the price of one.
Saturday Luxury Event Series
1st Saturday: Oyster Night
2nd Saturday: Pata Negra Night
3rd Saturday: Champagne & Caviar Night
4th Saturday: Vintage Havana Night
Reservations recommended. Limited seating for all special events.
Private Events & Corporate Gatherings

Marlowe’s is available for private celebrations and exclusive corporate evenings. Contact us to discuss your bespoke event.
Menu
Menu 2025/2026
All prices in Swiss Francs (CHF), incl. 8.1% VAT
Menu Classics
Old Fashioned — 18.00

Mint Julep — 18.00

Bees Knees — 18.00

French 75 — 23.00

Mary Pickford — 18.00

Sidecar — 18.00
Gin Cocktails
Negroni — 18.00

Charly Chaplin — 18.00

Southside — 18.00

Clover Club — 18.00

Aviation — 18.00
Vodka Cocktails
Cosmopolitan — 18.00

Garrison Lane — 18.00

Champ — 18.00

Polly Punch — 18.00

Bloody Mary — 18.00
Rum Cocktails
Rum Buck — 18.00

Rum Raisin — 23.00

Old Cuban — 18.00

Mojito — 18.00

Hillbilly — 18.00
Whiskey Cocktails
Dirty Old Bastard — 18.00

Blood and Sand — 18.00

Smoked Boulevardier — 18.00

Lynchburg Lemonade — 18.00

Manhattan — 18.00
Tequila Drinks
Mezcal Last Word — 18.00

Margarita — 18.00

Beachtwister — 18.00

Mexican Mint Smash — 18.00

The 212 — 18.00
Joker Drinks
Adas Sour — 18.00

Basil Smash — 18.00

Espresso Martini — 18.00

Port & Tonic — 18.00

Shelby Ginger — 18.00

Moscow Mule — 18.00

Tiefseetaucher — 28.00
Mocktails
The Fluffy Rose — 15.00

Lonesome Shelby — 16.00

Amaretto Sour — 16.00

Sober Tommy — 16.00

The Hillbilly Bobs No Ruckus — 16.00
Deals
Churchill Deal — 29.00

Upper Deck Deal — 22.00

Lower Deck Deal — 16.00
Sparkling & Champagne
Poggio Varenna Prosecco — 1 dl 9.50 / 7.5 dl 57.00

Lucien Marvaux Champagne — 1 dl 17.00 / 7.5 dl 105.00

Dorvelle-Rasquin Champagne — 7.5 dl 153.00
Beer
Talchnab, Frische Wuet — 2.5 dl 6.00 / 4 dl 8.00

Beer of the Month — Ask the bartender

Grubenhofer Weizenbier — 5 dl 9.50

Kalmbacher Feinsud — 3 dl 6.50 / 5 dl 9.00

KWNT Clear, Alcohol Free — 3 dl 6.50
Soft Drinks & Coffee
Sparkling & Still Water (5 dl) — 5.50

Fizzola / Zero (3 dl) — 5.50

Tonic / Ginger Ale / Ginger Beer / Bitter Lemon (2 dl) — 5.50

Fruit Juice Spritzer (5 dl) — 7.50

Verde Yerba (3 dl) — 6.50

Rossamaro — 6.00

Velanto — 6.00

Coffee / Espresso — 5.50

Tea & Rum — 8.50

Coffee Schnaps — 8.50
Gallery
A Glimpse Inside Marlowe’s

Browse our gallery for a taste of the Marlowe’s experience—from art deco interiors and intimate gatherings to signature cocktails and exclusive events.

[Gallery/Slideshow of high-quality images]
Reservations
Reserve Your Table
Book your seat at Marlowe’s Cocktail Bar & Cigar Lounge.

Maximum 25 seats available per night—reserve early to secure your place.
Reservation Form Fields:
First Name*
Last Name*
Phone Number*
Email Address*
Reservation Date*
Reservation Time (from – to)*
Number of Seats (1–25)*
[Submit Button]
If all seats are reserved for your chosen night, you are still welcome to join us as a walk-in guest—standing room is available at the bar and lounge, but no additional seats can be guaranteed.
You will receive a confirmation once your reservation is complete. For group bookings or special requests, please contact us directly.
Contact
Contact Marlowe’s

Address: Uferweg 14, 8999 Seeborn, Switzerland

Phone: 076 431 87 52

Email: contact@marlowes-example.ch

Website: www.marlowes-example.ch

Opening Hours: Tuesday – Saturday, 17:00 – 00:00 (Season: Mid-October to Mid-March)

Follow Us: Instagram | Facebook | LinkedIn | X (Twitter)

Getting Here: Conveniently located by the lake in Kilchberg. Parking is available.
Booking Section Technical Instructions
Integrate a booking form (Wix Bookings app or custom form) with the above fields and logic.
Enforce a hard cap of 25 reserved seats per night.
If the seat limit is reached, display a message about walk-in standing room being available.
Ensure the form is mobile-friendly and art deco styled.
Send all bookings to admin email (contact@marlowes-example.ch) and store in Wix dashboard.
Notify admin when a night is fully booked for seats.
Add reCAPTCHA or spam protection.
Additional Instructions for Designer
Platform: Build on Wix.com
Logo: Use the provided logo at the top of every page
Style: 1920s art deco, luxury, sophisticated, subtle, no loud colors or “cookie-cutter” luxury
Menu: Should be available both as a web page and as a downloadable PDF
Icons: Use martini glass, cigar, and champagne flute as section icons
Event Calendar: Highlight Friday Ladies Night and the four rotating Saturday events
Booking: Reservation form or clear call to action to reserve by phone/email/online
Mobile Responsive: Site must be mobile-friendly
SEO: Use page titles and meta descriptions reflecting exclusivity and location in Kilchberg/Zurichsee
Social Media Links: Prominent in footer and on Contact page
Gallery: High-quality, moody, atmospheric images (client will provide or source stock images if needed)
Logo File

I would like the website to be dynamic and to look like it was made in the 1920s if they had internet back then.

End of Brief

Target Market(s)

Target Market for Marlowe’s Cocktail Bar & Cigar Lounge Demographics: Age: 35–60 Income: CHF 200,000+ (regular guests), CHF 300,000+ (VIP guests) Location: Primarily Zurichsee enclaves (Kilchberg, surrounding lakeside communities), UHNWIs (Ultra-High-Net-Worth Individuals) with Swiss homes Profession/Background: Swiss finance elite Pharma executives Luxury watch CEOs Entrepreneurs Diplomats Old money families Psychographics & Interests: Appreciation for Cuban & Ravelin cigars, rare scotch & Swiss malts Enjoys lakeside ambiance and 1920s-inspired luxury Discreet, values privacy and exclusivity Prefers intelligent indulgence and after-work rituals Attracted to subtle spectacle, camaraderie, and personalized service Avoids loud groups, tourists, and casual drinkers Behavioral Traits: Regulars visit about once a week; 50% repeat, 50% new Willing to pay CHF 5,000+ for membership perks (though no program currently exists) Seeks a sanctuary from crowded city nightlife—prefers Marlowe’s for its refined, sophisticated, and exclusive atmosphere Summary: Marlowe’s is designed for Zurichsee’s discerning, high-income professionals and connoisseurs—people who value privacy, quality, and a sense of belonging in an exclusive yet welcoming environment.

Industry/Entity Type

Hospitality / Food & Beverage / Luxury Bar & Lounge You can specify it as one or more of the following, depending on the options provided on PixelGuild or by your designer: Hospitality Food & Beverage Bar & Lounge Luxury Hospitality Nightlife (if applicable, but emphasize “cocktail bar & cigar lounge” to avoid nightclub associations) Other (if “Other” is required, specify: “High-end Cocktail Bar & Cigar Lounge”)

Coding

Coded - Design and coding required

Number of Pages Required

5+ page

Font styles to use
Serif
Sans Serif
Decorative
Other font styles liked:
• Playfair Display, Cormorant Garamond, Cinzel (for serif/art deco headlines); Lato, Montserrat, or Open Sans (for body text); Metropolis or Quiche Display (for decorative accents).

Colors

Designer to choose colors to be used in the design.

Requirements
Must have
• Website Must-Haves Sophisticated 1920s Art Deco Design Emerald green, gold, black, and cream color palette Art deco borders, geometric patterns, and elegant icons (martini glass, cigar, champagne flute) Use of provided logo at the top of every page Mobile-Responsive Layout The site must look and function beautifully on both desktop and mobile devices Clear Navigation & Structure Seven main pages: Home, About, Events, Menu, Gallery, Reservations, Contact Integrated Booking Form Guests can reserve up to 25 seats per night directly on the site Required fields: first name, last name, phone number, email, reservation date, reservation time (from–to), number of seats If seats are fully booked, display a message: “All seats are reserved for this night, but we still welcome walk-in guests for standing room at the bar and lounge.” Booking notifications sent to admin email and/or stored in Wix dashboard Downloadable Menu Menu available as both a styled web page and a downloadable, print-friendly PDF Event Highlights Clearly showcase recurring events: Ladies Night (Fridays) and four rotating Saturday luxury events (Oyster Night, Pata Negra Night, Champagne & Caviar Night, Vintage Havana Night) High-Quality Gallery Gallery page with moody, atmospheric photos of the bar, cocktails, cigars, and events Contact & Location Information Address, phone, email, opening hours, map/directions, and social media links (Instagram, Facebook, LinkedIn, X/Twitter) Footer with all key contact details SEO-Ready Page titles and meta descriptions that reflect exclusivity, luxury, and Kilchberg/Zurichsee location Wix-Friendly Design Files Uncoded, layered design files (PSD, Figma, or XD) and all visual assets, ready for Wix implementation
Nice to have
• Nice-to-Haves for Marlowe’s Cocktail Bar & Cigar Lounge Website Animated Art Deco Details Subtle animated borders, transitions, or icon highlights to bring the 1920s luxury vibe to life. Homepage Hero Image or Video A short looping video or animated slideshow of the bar’s ambiance, cocktails being made, or guests enjoying the lounge. Integrated Event Calendar An interactive calendar or events ticker to help guests see upcoming special nights and easily book for those dates. Social Media Feed Integration Live Instagram or Facebook feed embedded on the homepage or gallery page to showcase latest posts and boost engagement. Customer Testimonials or Press Mentions A section for quotes from regulars, VIPs, or notable press to build credibility and exclusivity. Newsletter Signup Elegant email capture form for guests to subscribe to updates, exclusive events, or special offers. Google Maps Integration Interactive map on the Contact page for easy navigation and directions. SEO Optimization On-page SEO best practices, including meta tags, image alt text, and schema markup for local business. Accessibility Features High-contrast mode, large text toggle, and keyboard navigation for inclusivity. Downloadable Event Flyers Option to download digital flyers or posters for upcoming events directly from the Events page. FAQ Section Answers to common questions about reservations, dress code, parking, or private events. Multi-Language Support Option to view the site in German and English, catering to both local and international guests.
Should not have
• Should Not Haves for Marlowe’s Cocktail Bar & Cigar Lounge Website No Loud, Flashy, or “Nightclub” Design Elements Avoid neon colors, blinking animations, or anything resembling a modern club/bar scene. No “cookie-cutter luxury” or generic bar imagery. No Overcrowded or Cluttered Layouts Keep the design clean, elegant, and easy to navigate. Avoid excessive text blocks, too many pop-ups, or busy backgrounds. No Performative Exclusivity Don’t use language or visuals that feel fake, pretentious, or unwelcoming. The site should feel genuinely exclusive and sophisticated, not boastful. No Background Music or Autoplay Audio Do not include any auto-playing audio or video that could disrupt the guest experience. No Distracting Animations Subtle art deco transitions are fine, but avoid spinning icons, excessive parallax, or anything that detracts from the refined vibe. No Generic Stock Photos Avoid using cliché images of cocktails, cigars, or people that don’t reflect Marlowe’s unique ambiance. Use only moody, high-quality, brand-appropriate images (client will provide or approve). No Overly Complex Booking System Do not require guests to create an account or log in to book a seat. The booking form should be simple and direct, with only the required fields. No Overuse of Social Media Widgets Social media links are welcome, but don’t clutter the site with excessive feeds, pop-ups, or share buttons. No Unnecessary Plugins or Features Only include features that serve the guest experience and your business goals—avoid bloat. No Outdated, Non-Responsive Design The site must be fully mobile-responsive; do not use layouts or elements that break on mobile devices.

```html
<!DOCTYPE html>
<html lang="en">
<head>
<meta charset="utf-8">
<title>Marlowe’s Cocktail Bar &amp; Cigar Lounge</title>
<link rel="stylesheet" href="https://fonts.googleapis.com/css2?family=Playfair+Display:wght@400;500&family=Montserrat:wght@400;500;600;700&display=swap">
<style>
:root{
  --gold:#c49a6c;
  --gold-line:#e6d6c2;
  --ink:#1c1c1c;
  --text:#3a3a3a;
  --black:#0b0b0b;
  --mist:#f3f3f3;
  --white:#ffffff;
}
*{margin:0;padding:0;box-sizing:border-box}
html,body{width:1200px;height:3849px;overflow:hidden;background:var(--white)}
body{font-family:"Montserrat",sans-serif;color:var(--text);position:relative}
section,header,footer{position:relative;width:1200px}
.abs{position:absolute}
.btn{position:absolute;display:flex;align-items:center;justify-content:center;background:var(--gold);color:var(--white);font-weight:600;font-size:9.5px;letter-spacing:.6px;text-transform:uppercase;text-decoration:none}
.heading{font-family:"Playfair Display",serif;font-weight:400;color:var(--ink);font-size:42px;line-height:1}
.photo{position:absolute;overflow:hidden}

/* header + hero */
.hero{height:562px;background:radial-gradient(ellipse at 45% 40%,#7a4a22 0%,#3d2412 40%,#150d07 80%)}
.hero-shade{position:absolute;inset:0;background:linear-gradient(rgba(0,0,0,.35),rgba(0,0,0,.2) 60%,rgba(0,0,0,.35))}
.nav-bar{position:absolute;left:0;top:0;width:1200px;height:63px;background:var(--black)}
.brand{position:absolute;left:107px;top:10px;font-family:"Playfair Display",serif;font-size:25px;color:var(--white);font-weight:500}
.nav a{position:absolute;top:25px;font-size:10px;font-weight:600;color:var(--white);text-decoration:none;letter-spacing:.3px;transform:translateX(-50%)}
.nav a.active{color:var(--gold)}
.hero-title{position:absolute;left:0;width:1200px;top:212px;text-align:center;font-family:"Playfair Display",serif;font-weight:400;font-size:43px;line-height:53px;color:var(--white)}
.hero-sub{position:absolute;left:0;width:1200px;top:327px;text-align:center;font-size:15px;font-weight:500;color:var(--white);letter-spacing:.4px}

/* new era */
.era{height:629px}
.era-text{position:absolute;left:719px;top:230px;width:275px;font-size:12px;line-height:22.5px;color:var(--ink)}
.era-text p+p{margin-top:22px}

/* signature */
.signature{height:488px;background:var(--mist)}
.exp{position:absolute;width:260px;text-align:center;transform:translateX(-50%)}
.exp svg{display:block;margin:0 auto}
.exp h3{font-family:"Playfair Display",serif;font-weight:400;font-size:16.5px;color:var(--ink);margin-top:12px}
.exp p{font-size:9.5px;line-height:14.5px;color:var(--text);margin-top:8px;padding:0 8px}
.divider{position:absolute;top:176px;width:1px;height:149px;background:#dcdcdc}

/* hosts */
.hosts{height:562px;background:linear-gradient(#ffffff,#f2f2f2)}
.hosts-text{position:absolute;left:524px;top:210px;width:450px;font-size:14.5px;line-height:30px;color:var(--text)}

/* gallery */
.gallery{height:877px}

/* reserve */
.reserve{height:396px;background:linear-gradient(120deg,#f4efe8,#f6f1ee 45%,#f3ece4)}
.card{position:absolute;top:196px;width:250px;height:124px;background:rgba(255,255,255,.85);border:1.5px solid var(--gold-line);text-align:center}
.card .badge{position:absolute;left:50%;top:-34px;width:68px;height:68px;margin-left:-34px;border-radius:50%;background:var(--white);border:1.5px solid var(--gold-line);display:flex;align-items:center;justify-content:center}
.card h4{font-family:"Playfair Display",serif;font-weight:400;font-size:16px;color:var(--ink);margin-top:52px}
.card p{font-size:11px;color:var(--text);margin-top:8px}

/* footer */
.footer{height:335px;background:var(--black);color:var(--white)}
.foot-brand{position:absolute;left:0;width:1200px;top:48px;text-align:center;font-family:"Playfair Display",serif;font-size:34px;font-weight:500}
.rule{position:absolute;left:200px;width:800px;height:1px;background:#3a3a3a}
.foot-info{position:absolute;left:0;width:1200px;top:162px;text-align:center;font-size:11px}
.foot-info b{color:var(--gold);font-weight:500}
.foot-info .sep{color:#777;margin:0 20px}
.socials{position:absolute;top:231px;left:540px;display:flex;gap:6px}
.socials span{width:26px;height:26px;border:1px solid #bbb;border-radius:50%;display:block;position:relative}
.socials span::after{content:"";position:absolute;left:9px;top:9px;width:7px;height:7px;border-radius:50%;background:#ddd}
.copy{position:absolute;left:0;width:1200px;top:281px;text-align:center;font-size:11px}
.copy b{color:var(--gold);font-weight:400}
</style>
</head>
<body>

<header class="hero">
  <div class="photo" style="inset:0" role="img" aria-label="Two crystal tumblers of amber cocktail with peach slices on a silver tray, white roses behind"></div>
  <div class="hero-shade"></div>
  <div class="nav-bar">
    <div class="brand">marlowes</div>
    <nav class="nav">
      <a class="active" style="left:559px">HOME</a>
      <a style="left:632px">ABOUT</a>
      <a style="left:710px">EVENTS</a>
      <a style="left:784px">MENU</a>
      <a style="left:862px">GALLERY</a>
      <a style="left:965px">RESERVATIONS</a>
      <a style="left:1068px">CONTACT</a>
    </nav>
  </div>
  <h1 class="hero-title">Zurich’s Most Exclusive Cocktail<br>Bar &amp; Cigar Lounge</h1>
  <p class="hero-sub">TIMELESS SOPHISTICATION. INTELLIGENT INDULGENCE. A SANCTUARY BY THE LAKE.</p>
  <a class="btn" style="left:509px;top:378px;width:181px;height:37px">Reserve your table</a>
</header>

<section class="era">
  <svg class="abs" style="left:0;top:0" width="1200" height="629">
    <circle cx="568" cy="300" r="254" fill="none" stroke="var(--gold-line)" stroke-width="1.2"/>
    <line x1="403" y1="146" x2="1001" y2="146" stroke="var(--gold-line)" stroke-width="1.2"/>
  </svg>
  <h2 class="heading abs" style="left:200px;top:70px">A new era on the lake</h2>
  <div class="photo" style="left:200px;top:216px;width:206px;height:275px;border-radius:0 110px 0 110px / 0 140px 0 70px;background:linear-gradient(160deg,#6a4424,#3a2414 55%,#1e130b)" role="img" aria-label="Wooden bar counter with lit shelves of bottles"></div>
  <div class="photo" style="left:430px;top:189px;width:226px;height:325px;border-radius:113px 113px 0 0;background:linear-gradient(170deg,#8a6238,#4a3624 50%,#5a2e2a 85%,#2a1c14)" role="img" aria-label="Long bar with warm pendant lights and leather stools"></div>
  <div class="era-text">
    <p>Marlowe’s invites you into a world where elegance meets camaraderie, and every visit feels like a privilege.</p>
    <p>Step through our doors and discover a connoisseur’s sanctuary inspired by the golden age of the 1920s—reimagined for Zurich’s most discerning guests.</p>
  </div>
  <a class="btn" style="left:719px;top:440px;width:146px;height:36px">Explore more</a>
</section>

<section class="signature">
  <h2 class="heading abs" style="left:0;width:1200px;text-align:center;top:83px">Signature experiences await</h2>
  <div class="exp" style="left:324px;top:196px">
    <svg width="46" height="40" viewBox="0 0 46 40" fill="none" stroke="#222" stroke-width="1.6"><path d="M6 14h34l-4 10a13 13 0 0 1-26 0z"/><path d="M23 37v-4M16 37h14"/><circle cx="23" cy="7" r="4" stroke="var(--gold)"/><path d="M10 12c-3-4-7-2-7 1M36 12c3-4 7-2 7 1" stroke="var(--gold)"/></svg>
    <h3>Ladies Night, Every Friday</h3>
    <p>Two cocktails for the price of one, exclusively for the ladies.</p>
  </div>
  <div class="divider" style="left:462px"></div>
  <div class="exp" style="left:600px;top:183px">
    <svg width="42" height="44" viewBox="0 0 42 44" fill="none" stroke="#222" stroke-width="1.6"><rect x="3" y="6" width="36" height="35"/><path d="M3 13h36"/><path d="M9 2v8M16 2v8M23 2v8M30 2v8M36 2v8"/><circle cx="21" cy="24" r="5" stroke="var(--gold)"/><path d="M21 29v8" stroke="var(--gold)"/></svg>
    <h3>Saturday Event Series</h3>
    <p>Oyster night, pata negra night, champagne &amp; caviar night, and vintage havana night—each a celebration of taste and refinement.</p>
  </div>
  <div class="divider" style="left:737px"></div>
  <div class="exp" style="left:875px;top:183px">
    <svg width="42" height="44" viewBox="0 0 42 44" fill="none" stroke="#222" stroke-width="1.6"><path d="M5 14h32L21 28z"/><path d="M21 28v12M13 41h16"/><path d="M28 4l6 6M31 3l-1 4" stroke="var(--gold)"/><circle cx="33" cy="12" r="3" stroke="var(--gold)"/></svg>
    <h3>Curated Cocktails &amp; Cigars</h3>
    <p>Savor our expertly crafted cocktails, rare spirits, and a handpicked selection of premium cigars.</p>
  </div>
  <a class="btn" style="left:509px;top:375px;width:181px;height:36px">Reserve your table</a>
</section>

<section class="hosts">
  <div class="abs" style="left:257px;top:114px;width:230px;height:366px;border:1.2px solid var(--gold-line);border-radius:137px 137px 0 0"></div>
  <div class="photo" style="left:200px;top:75px;width:275px;height:393px;border-radius:138px 138px 0 0;background:radial-gradient(ellipse at 40% 70%,#6a4a2c,#2a2018 55%,#0f1620)" role="img" aria-label="Crystal whisky glass and lit cigar on a glass ashtray in a dim lounge"></div>
  <h2 class="heading abs" style="left:524px;top:141px">Meet your hosts</h2>
  <p class="hosts-text">In 2025, a new partnership brings fresh energy to marlowe’s. hospitality expert orla vantrisk (quillhaven productions) joins forces with renowned bar professional teodor brask (shaker at the ready) to elevate your experience and set a new standard for luxury in zurichsee.</p>
  <a class="btn" style="left:524px;top:387px;width:174px;height:36px">Contact us today!</a>
</section>

<section class="gallery">
  <h2 class="heading abs" style="left:0;width:1200px;text-align:center;top:82px">Photo gallery</h2>
  <div class="photo" style="left:106px;top:157px;width:312px;height:362px;background:linear-gradient(170deg,#3a3a3e,#5a4228 55%,#2a2018)" role="img" aria-label="Gold-framed back bar with illuminated counter and stools"></div>
  <div class="photo" style="left:106px;top:544px;width:312px;height:200px;background:radial-gradient(ellipse at 50% 55%,#6b4a34,#1a1412 65%)" role="img" aria-label="Cocktail glasses and jigger on a dark bar top"></div>
  <div class="photo" style="left:444px;top:157px;width:312px;height:281px;background:linear-gradient(160deg,#4a3a2a,#b2543e 45%,#5a7a3a 75%,#2a2a20)" role="img" aria-label="Colourful mojito and fruit cocktails with garnish"></div>
  <div class="photo" style="left:444px;top:463px;width:312px;height:281px;background:linear-gradient(170deg,#8a6238,#4a3624 50%,#5a2e2a 85%,#2a1c14)" role="img" aria-label="Long bar counter with pendant lights and leather stools"></div>
  <div class="photo" style="left:781px;top:157px;width:313px;height:199px;background:radial-gradient(ellipse at 60% 50%,#8a5a30,#3a2416 70%)" role="img" aria-label="Whisky glass and cigar in front of a leather chesterfield"></div>
  <div class="photo" style="left:781px;top:381px;width:313px;height:363px;background:linear-gradient(160deg,#4a5060,#6a5a52 45%,#2a2430)" role="img" aria-label="Guests toasting with beer mugs at a table"></div>
  <a class="btn" style="left:542px;top:769px;width:115px;height:38px">View all</a>
</section>

<section class="reserve">
  <div class="photo" style="inset:0;opacity:.5;background:radial-gradient(ellipse at 30% 60%,#efe3d2,transparent 60%),radial-gradient(ellipse at 75% 70%,#f1dcd6,transparent 55%)" role="img" aria-label="Faded background of cocktails on a bar"></div>
  <h2 class="heading abs" style="left:0;width:1200px;text-align:center;top:90px">Reserve your table</h2>
  <div class="card" style="left:200px">
    <div class="badge"><svg width="32" height="32" viewBox="0 0 32 32" fill="none" stroke="#222" stroke-width="1.5"><path d="M7 5l5 1 2 6-3 2a14 14 0 0 0 7 7l2-3 6 2 1 5-3 2C12 27 5 20 5 8z"/><circle cx="24" cy="8" r="5" fill="var(--gold)" stroke="none"/></svg></div>
    <h4>Phone</h4><p>076 431 87 52</p>
  </div>
  <div class="card" style="left:475px">
    <div class="badge"><svg width="32" height="32" viewBox="0 0 32 32" fill="none" stroke="#222" stroke-width="1.5"><path d="M4 13l12-9 12 9v14H4z"/><path d="M4 13l12 9 12-9"/><rect x="11" y="9" width="10" height="8" stroke="var(--gold)"/></svg></div>
    <h4>Email</h4><p>contact@marlowes-example.ch</p>
  </div>
  <div class="card" style="left:750px">
    <div class="badge"><svg width="32" height="32" viewBox="0 0 32 32" fill="none" stroke="#222" stroke-width="1.5"><circle cx="14" cy="14" r="10" stroke-dasharray="3 2"/><path d="M16 16l10 4-4 2-2 4z" stroke="var(--gold)"/></svg></div>
    <h4>Online</h4><p>www.marlowes-example.ch</p>
  </div>
</section>

<footer class="footer">
  <div class="foot-brand">marlowes</div>
  <div class="rule" style="top:139px"></div>
  <p class="foot-info"><b>&#9679; Address:</b> Uferweg 14, 8999 Seeborn, Switzerland<span class="sep">|</span><b>&#9675; Open:</b> Wednesday–Sunday, 18:00–01:00 | November–April</p>
  <div class="rule" style="top:200px"></div>
  <div class="socials"><span></span><span></span><span></span><span></span></div>
  <p class="copy">© 2025 <b>Marlowes Bar</b>. All Rights Reserved.</p>
</footer>

</body>
</html>
```